Home page makeover

Take my existing home page, www.maplecrestledger.com and redesign layout to look more current considering today's touch design prevalence.
Reuse existing elements or suggest improved ones if available.
I generally have average CSS and HTML skills using div containers, defining lists and using columns to create the code to support the layout.
Updates
Just wanted to send out a quick message to thank all of you for your submissions. Many of you offered nice designs, but unfortunately could only choose one.
Target Market(s)
Generally targeting individuals with some assets for retirement. Basically your average working professional or business owner.
Industry/Entity Type
It Support
Look and feel
Each slider illustrates characteristics of the customer's brand and the style your logo design should communicate.

```html
<!DOCTYPE html>
<html lang="en">
<head>
<meta charset="utf-8">
<title>Maplecrest Ledger – Retirement Plans</title>
<link href="https://fonts.googleapis.com/css2?family=Questrial&family=Open+Sans:wght@400;700;800&display=swap" rel="stylesheet">
<style>
:root{
  --green:#8dc63f;
  --green-ring:#c6e39a;
  --ink:#222;
  --muted:#8a8a8a;
  --body:#555;
  --band:#f2f2f2;
  --footer:#2f2f2f;
  --grey-btn:#9b9b9b;
}
*{margin:0;padding:0;box-sizing:border-box}
html,body{width:819px;height:1200px;overflow:hidden;background:#fff}
body{font-family:Arial,Helvetica,sans-serif;color:var(--ink)}
.page{position:relative;width:819px;height:1200px}
.abs{position:absolute}

/* header */
.brand{left:103px;top:22px;display:flex;align-items:center;gap:8px;font-family:'Questrial',sans-serif;font-size:24px;color:#3f7a1c}
.brand .mark{width:22px;height:22px;background:var(--green);border-radius:3px}
.account{top:12px;right:103px;display:flex;gap:8px}
.btn{display:inline-block;color:#fff;font-size:10px;padding:4px 10px;border-radius:2px}
.btn.in{background:var(--green)}
.btn.up{background:var(--grey-btn)}
.nav{top:50px;right:103px;display:flex;gap:28px;font-size:11px;color:#444}

/* hero */
.hero{left:0;top:83px;width:819px;height:317px;
  background:linear-gradient(180deg,#8fb6d8 0%,#c9dbe8 28%,#6e7f6d 48%,#6f9a3a 62%,#8bbf3a 78%,#5f7f48 100%)}
.hero .arrow{top:135px}
.hero-title{left:148px;top:188px;font-family:'Open Sans',sans-serif;font-weight:800;font-size:22px;color:#fff;letter-spacing:.2px}
.hero-text{left:148px;top:217px;width:290px;font-size:10px;line-height:12px;color:#fff}

/* signup band */
.band{left:0;top:400px;width:819px;height:59px;background:var(--band)}
.perks{left:103px;top:413px;font-size:10.5px;line-height:21px;color:#222}
.perks li{list-style:none;display:flex;align-items:center;gap:6px}
.field{top:418px;width:136px;height:24px;background:#fff;border:1px solid #e2e2e2;font-size:10.5px;color:#aaa;padding:5px 7px}
.band-cta{left:626px;top:419px;width:90px;height:23px;background:var(--green);color:#fff;font-size:11px;text-align:center;line-height:23px;border-radius:2px}

/* steps */
.step{width:200px;text-align:center}
.step .ring{width:80px;height:80px;margin:0 auto;border-radius:50%;background:var(--green);border:3px solid var(--green-ring);display:flex;align-items:center;justify-content:center}
.step h2{font-family:'Questrial',sans-serif;font-weight:400;font-size:15px;margin-top:10px;color:#111}
.step p{font-size:9px;line-height:11px;color:var(--muted);margin-top:5px}

.rule{left:116px;width:587px;height:1px;background:linear-gradient(90deg,transparent,#e6e6e6,transparent)}

/* features */
.section-title{font-family:'Questrial',sans-serif;font-size:16px;color:#222;text-align:center}
.features{left:102px;top:740px;width:305px}
.feature{display:flex;gap:8px;margin-bottom:12px}
.feature .dot{flex:none;width:30px;height:30px;border-radius:50%;background:var(--green);display:flex;align-items:center;justify-content:center;color:#fff;font-weight:700;font-size:15px}
.feature p{font-size:7.5px;line-height:12.8px;color:var(--body)}

.video{left:445px;top:735px;width:261px;height:176px;box-shadow:0 1px 4px rgba(0,0,0,.2)}
.video .scene{width:261px;height:159px;background:linear-gradient(180deg,#8fb7d9 0%,#c3d8e6 30%,#4b7ea8 45%,#3d6f95 60%,#7d8a4a 78%,#6e9a34 100%);position:relative}
.video .play{position:absolute;left:113px;top:62px}
.video .controls{height:17px;background:linear-gradient(#f4f4f4,#d9d9d9);position:relative;font-size:5px;color:#666}

/* testimonials */
.quote{width:178px;background:#fafafa;box-shadow:1px 1px 3px rgba(0,0,0,.15);font-size:8.5px;font-style:italic;line-height:11px;color:#555;padding:10px 9px}
.quote:after{content:"";position:absolute;left:28px;bottom:-10px;border-left:0 solid transparent;border-right:10px solid transparent;border-top:10px solid #fafafa}
.who{font-size:8.5px;color:#222}
.who span{color:var(--green)}

footer{left:0;top:1150px;width:819px;height:50px;background:var(--footer);color:#fff;font-size:8.5px;text-align:center;line-height:15px;padding-top:11px}
</style>
</head>
<body>
<div class="page">

  <header>
    <div class="abs brand"><span class="mark"></span>Maplecrest Ledger</div>
    <div class="abs account"><span class="btn in">Sign In</span><span class="btn up">Sign up</span></div>
    <nav class="abs nav"><span>Home</span><span>About us</span><span>Services</span><span>Testimonials</span><span>Contact us</span></nav>
  </header>

  <section class="abs hero" role="img" aria-label="Photo of an alpine valley with a village, green meadows and a stream under a cloudy sky">
    <svg class="abs arrow" style="left:88px" width="16" height="42" viewBox="0 0 16 42"><path d="M15 1 L1 21 L15 41" stroke="#fff" stroke-width="1.2" fill="none" opacity=".8"/></svg>
    <svg class="abs arrow" style="left:716px" width="16" height="42" viewBox="0 0 16 42"><path d="M1 1 L15 21 L1 41" stroke="#fff" stroke-width="1.2" fill="none"/></svg>
  </section>
  <h1 class="abs hero-title">RETIREMENT PLANS</h1>
  <p class="abs hero-text">Lorem ipsum dolor sit amet, consectetur adipiscing elit. Etiam ante massa, consectetur vel rhoncus a eget.</p>

  <section class="abs band"></section>
  <ul class="abs perks">
    <li><svg width="10" height="9" viewBox="0 0 10 9"><path d="M1 5 L4 8 L9 1" stroke="#8dc63f" stroke-width="2" fill="none"/></svg>Only $19.99 For a One Year Membership</li>
    <li><svg width="10" height="9" viewBox="0 0 10 9"><path d="M1 5 L4 8 L9 1" stroke="#8dc63f" stroke-width="2" fill="none"/></svg>Only $9.99 Per Year After That</li>
  </ul>
  <div class="abs field" style="left:339px">Your Name</div>
  <div class="abs field" style="left:482px">Email Address</div>
  <div class="abs band-cta">Sign up</div>

  <section>
    <div class="abs step" style="left:92px;top:494px">
      <div class="ring"><svg width="42" height="34" viewBox="0 0 42 34" fill="#fff"><rect x="0" y="0" width="34" height="8" rx="4"/><rect x="0" y="11" width="28" height="8" rx="4"/><rect x="0" y="22" width="24" height="8" rx="4"/><circle cx="31" cy="22" r="6" fill="none" stroke="#fff" stroke-width="3"/><path d="M35 26 L41 32" stroke="#fff" stroke-width="3"/></svg></div>
      <h2>IDENTIFY</h2>
      <p>Lorem ipsum dolor sit amet, consectetur adipiscing elit. Nullam semper eu diam eget laoreet. Nunc non orci eu augue.</p>
    </div>
    <div class="abs step" style="left:310px;top:494px">
      <div class="ring"><svg width="34" height="38" viewBox="0 0 34 38" fill="none" stroke="#fff" stroke-width="2.2"><path d="M3 2 H20 L26 8 V20"/><path d="M3 2 V36 H18"/><path d="M8 11 H18 M8 17 H16 M8 23 H13"/><circle cx="24" cy="28" r="8"/><path d="M24 23 V28 H28"/></svg></div>
      <h2>PLAN</h2>
      <p>Lorem ipsum dolor sit amet, consectetur adipiscing elit. Nullam semper eu diam eget laoreet. Nunc non orci eu augue.</p>
    </div>
    <div class="abs step" style="left:527px;top:494px">
      <div class="ring"><svg width="42" height="38" viewBox="0 0 42 38" fill="none" stroke="#fff" stroke-width="2.2"><path d="M18 9 Q28 -2 38 9 Z" fill="#fff"/><path d="M28 8 L22 30"/><circle cx="10" cy="16" r="3" fill="#fff"/><path d="M4 28 L12 20 L22 28 M2 34 H40"/></svg></div>
      <h2>RETIRE</h2>
      <p>Lorem ipsum dolor sit amet, consectetur adipiscing elit. Nullam semper eu diam eget laoreet. Nunc non orci eu augue.</p>
    </div>
  </section>

  <div class="abs rule" style="top:677px"></div>

  <h2 class="abs section-title" style="left:154px;top:709px;width:200px">FEATURES</h2>
  <section class="abs features">
    <div class="feature"><span class="dot">$</span><p>Identify and project your retirement needs and expectations including basic living expenses, housing costs, recreation, big ticket non-recurring items, medical and nursing home care.</p></div>
    <div class="feature"><span class="dot"><svg width="16" height="13" viewBox="0 0 16 13" fill="#fff"><ellipse cx="8" cy="7" rx="7" ry="5"/><rect x="4" y="10" width="2" height="3"/><rect x="10" y="10" width="2" height="3"/></svg></span><p>Identify and project all your sources of retirement income including retirement savings, other savings, pension plans, Social Security, life insurance and working part-time during retirement for a period of time.</p></div>
    <div class="feature"><span class="dot"><svg width="16" height="14" viewBox="0 0 16 14" fill="#fff"><path d="M8 0 L16 7 H13 V14 H3 V7 H0 Z"/></svg></span><p>Strategize tapping into the equity of your real estate including swapping your primary residence for a different home or retirement area, or selling and renting.</p></div>
    <div class="feature"><span class="dot"><svg width="16" height="16" viewBox="0 0 16 16" fill="none" stroke="#fff" stroke-width="2"><path d="M2 2 Q2 12 8 14 Q14 12 14 2"/><path d="M8 4 V13"/></svg></span><p>Save your work so you can return, revisit and edit your retirement plan at a later date.</p></div>
  </section>

  <div class="abs video">
    <div class="scene" role="img" aria-label="Video still of two wooden lawn chairs on a grassy bluff overlooking the sea">
      <svg class="play" width="34" height="34" viewBox="0 0 34 34"><circle cx="17" cy="17" r="15.5" fill="rgba(255,255,255,.15)" stroke="#fff" stroke-width="2"/><path d="M13 10 L24 17 L13 24 Z" fill="#fff"/></svg>
    </div>
    <div class="controls">
      <svg class="abs" style="left:6px;top:4px" width="8" height="9" viewBox="0 0 8 9"><path d="M0 0 L8 4.5 L0 9Z" fill="#555"/></svg>
      <div class="abs" style="left:24px;top:7px;width:130px;height:3px;background:#888;border-radius:2px"></div>
      <div class="abs" style="left:24px;top:7px;width:63px;height:3px;background:#e23a4a;border-radius:2px"></div>
      <div class="abs" style="left:84px;top:5px;width:7px;height:7px;border-radius:50%;background:#eee;border:1px solid #888"></div>
      <span class="abs" style="left:159px;top:5px">3:47 / 9:29</span>
      <svg class="abs" style="left:192px;top:5px" width="8" height="7" viewBox="0 0 8 7"><path d="M0 2 H2 L5 0 V7 L2 5 H0Z" fill="#555"/></svg>
      <div class="abs" style="left:204px;top:7px;width:32px;height:3px;background:#555;border-radius:2px"></div>
      <div class="abs" style="left:248px;top:4px;width:8px;height:8px;border:1px solid #666"></div>
    </div>
  </div>

  <div class="abs rule" style="top:960px"></div>

  <h2 class="abs section-title" style="left:310px;top:986px;width:200px;font-size:19px">TESTIMONIALS</h2>
  <section>
    <blockquote class="abs quote" style="left:103px;top:1029px">This site is a great place to get a handle on your retirement strategy.</blockquote>
    <p class="abs who" style="left:114px;top:1094px">Chris, <span>New Jersey</span></p>
    <blockquote class="abs quote" style="left:320px;top:1029px">It's the only retirement projection tool for the average user that puts it all together.</blockquote>
    <p class="abs who" style="left:331px;top:1104px">Jim, <span>New York</span></p>
    <blockquote class="abs quote" style="left:537px;top:1029px">I can see professionals using this site to validate their existing retirement plans.</blockquote>
    <p class="abs who" style="left:549px;top:1094px">Jim, <span>New Jersey</span></p>
  </section>

  <footer class="abs">
    Copyright © 2013 Maplecrest Ledger, Inc. All rights reserved.<br>
    Terms and Conditions &nbsp;|&nbsp; Privacy Policy
  </footer>

</div>
</body>
</html>
```